Velmont Recycling needs a new web design

We need a new web design for our company based in Austin, TX. We resell and recycling electronics such as laptops, computer components, Zelvos, Quorbs, etc. Since our inception over ten years ago, we’ve become one of the premier electronics recycling and remarketing companies in Austin, Texas.

```html
<!DOCTYPE html>
<html lang="en">
<head>
<meta charset="utf-8">
<title>Velmont Recycling</title>
<link href="https://fonts.googleapis.com/css2?family=Montserrat:wght@600;700&family=Open+Sans:wght@400;600;700&family=Roboto+Slab:wght@400;700&display=swap" rel="stylesheet">
<style>
:root{
  --blue:#1f5fae;
  --blue-dark:#174f96;
  --blue-band:#1a5cad;
  --blue-band2:#2166b8;
  --navy:#0f3e5e;
  --orange:#f5900f;
  --teal:#1b8a9a;
  --red:#e2332c;
  --ink:#222;
  --grey-text:#555;
  --light:#f2f2f2;
  --footer:#e6e6e6;
  --rule:#d8d8d8;
}
*{margin:0;padding:0;box-sizing:border-box}
html,body{width:1200px;height:4091px;overflow:hidden}
body{font-family:"Open Sans",sans-serif;color:var(--ink);background:#fff;position:relative}
.abs{position:absolute}
.brand{display:flex;align-items:center;gap:14px;font-family:"Roboto Slab",serif;font-weight:700;color:var(--blue);font-size:30px;line-height:1}
.brand-dot{width:58px;height:58px;border-radius:50%;background:var(--blue);flex:none}

/* header */
.site-header{position:absolute;left:0;top:0;width:1200px;height:118px;background:#fff}
.site-header .brand{position:absolute;left:130px;top:26px}
.follow{position:absolute;left:680px;top:30px;display:flex;align-items:center;gap:10px;font-size:11px;font-weight:700;color:#333}
.soc{width:24px;height:24px;border-radius:50%;background:var(--blue);display:inline-block}
.soc.b{background:#1da1f2}.soc.c{background:#0e4f86}
.callnow{position:absolute;left:908px;top:20px;display:flex;gap:10px;align-items:center}
.callnow .ph{width:28px;height:28px}
.callnow small{display:block;font-size:10px;font-weight:700;color:#333}
.callnow strong{display:block;font-size:20px;color:var(--blue);font-weight:700}
.nav{position:absolute;left:620px;top:78px;display:flex;gap:30px;font-size:13px;font-weight:700;color:#222}
.nav a{color:inherit;text-decoration:none;padding-bottom:6px}
.nav a.active{color:var(--blue);border-bottom:3px solid var(--blue)}

/* hero */
.hero{position:absolute;left:0;top:118px;width:1200px;height:556px;background:linear-gradient(135deg,#3b5a3a 0%,#24402e 30%,#2f3f55 55%,#4a5b3c 80%,#2c3a2a 100%)}
.hero-title{position:absolute;left:0;width:1200px;top:170px;text-align:center;color:#fff;font-family:"Montserrat",sans-serif;font-weight:700;font-size:40px;line-height:1.2;letter-spacing:1px}
.btn{display:inline-block;background:var(--blue);color:#fff;font-weight:700;font-size:14px;padding:12px 26px;letter-spacing:.5px}
.hero .btn{position:absolute;left:520px;top:292px;border:2px solid #fff;font-size:16px;padding:12px 30px}
.dots{position:absolute;left:530px;top:484px;display:flex;gap:16px}
.dots i{width:10px;height:10px;border-radius:50%;background:#fff;opacity:.6}
.dots i:first-child{opacity:1}

/* welcome */
.feature{position:absolute;left:175px;display:flex;align-items:center;gap:20px;font-size:18px;color:#333;line-height:1.35}
.feature .ic{width:78px;height:78px;border-radius:50%;border:3px solid #ccc;display:flex;align-items:center;justify-content:center}
.feature-rule{position:absolute;left:178px;width:300px;height:1px;background:var(--rule)}
.vrule{position:absolute;left:494px;top:740px;width:6px;height:390px;background:#ececec}
.welcome{position:absolute;left:560px;top:770px;width:470px}
.welcome h3{font-size:15px;font-weight:700;letter-spacing:.5px}
.welcome h2{font-family:"Roboto Slab",serif;color:var(--blue);font-size:30px;margin:8px 0 26px}
.welcome p{font-size:14px;line-height:1.65;color:var(--grey-text);margin-bottom:22px}

/* services */
.services{position:absolute;left:0;top:1200px;width:1200px;height:750px;background:linear-gradient(180deg,#efefef,#f4f4f4)}
.services svg.slant{position:absolute;left:0;top:0}
.sec-title{position:absolute;left:0;width:1200px;text-align:center;font-family:"Roboto Slab",serif;color:var(--blue);font-size:30px}
.sec-title::after{content:"";display:block;width:60px;height:2px;background:var(--blue);margin:16px auto 0}
.svc{position:absolute;width:300px;text-align:center}
.svc svg{display:block;margin:0 auto 16px}
.svc h4{font-family:"Roboto Slab",serif;font-size:14px;line-height:1.45;color:#222;font-weight:400;margin-bottom:12px}
.svc p{font-size:12.5px;line-height:1.45;color:#555}
.grid-v{position:absolute;width:1px;background:var(--rule)}
.grid-h{position:absolute;height:1px;background:var(--rule)}

/* capability */
.cap-list{position:absolute;width:180px;font-size:12px;line-height:1.45;color:#333}
.cap-list h5{font-size:14px;font-weight:700;margin-bottom:4px;color:#222}

/* benefit */
.benefit-band{position:absolute;left:0;top:3033px;width:1200px;height:494px;background:var(--blue-band)}
.benefit-band .half2{position:absolute;left:600px;top:0;width:600px;height:494px;background:var(--blue-band2)}
.benefit-col{position:absolute;top:70px;width:440px;color:#fff}
.benefit-col .hd{display:flex;gap:18px;align-items:center;font-family:"Montserrat",sans-serif;font-weight:700;font-size:25px;line-height:1.15}
.benefit-col ul{list-style:none;margin-top:40px;font-size:13px;line-height:1.55}
.benefit-col li{position:relative;padding-left:40px;padding-bottom:14px;margin-bottom:14px;border-bottom:1px solid rgba(255,255,255,.2)}
.benefit-col li::before{content:"›";position:absolute;left:10px;top:-3px;font-size:18px}
.btn-w{display:inline-block;background:#fff;color:var(--blue);font-weight:700;font-size:13px;padding:9px 16px;margin-top:16px}

/* contact strip */
.help{position:absolute;left:0;top:3527px;width:1200px;height:183px;background:#fff}
.help .sep{position:absolute;left:598px;top:0;width:1px;height:183px;background:var(--rule)}
.help .q{position:absolute;left:350px;top:52px;font-family:"Montserrat",sans-serif;font-size:17px;font-weight:700}
.help .q span{color:#9bb7d8}
.help .num{position:absolute;left:280px;top:82px;font-family:"Montserrat",sans-serif;color:var(--blue);font-size:38px;font-weight:600}
.help .sub{position:absolute;left:648px;top:52px;font-family:"Montserrat",sans-serif;font-size:17px;font-weight:700}
.help .sub span{color:#9bb7d8}
.help form{position:absolute;left:648px;top:88px;width:310px;height:36px;border:1px solid #ccc;display:flex}
.help input{flex:1;border:0;padding-left:34px;font-size:12px;font-family:inherit}
.help button{width:38px;background:var(--blue);border:0;color:#fff;font-size:18px}

/* footer */
.site-footer{position:absolute;left:0;top:3710px;width:1200px;height:381px;background:var(--footer)}
.site-footer .brand{position:absolute;left:140px;top:102px;font-size:34px}
.fcol{position:absolute;top:70px;font-size:12px;line-height:1.7;color:#333}
.fcol h6{font-size:12px;font-weight:700;color:var(--blue);margin-bottom:12px}
.fcol .row{display:flex;gap:12px;margin-bottom:14px;align-items:flex-start}
.fcol .sr{display:flex;gap:10px;align-items:center;margin-bottom:14px}
.copy{position:absolute;left:0;width:1200px;top:328px;text-align:center;font-size:11px;color:#333}
.copy-rule{position:absolute;left:140px;width:920px;top:310px;height:1px;background:#cfcfcf}
</style>
</head>
<body>

<header class="site-header">
  <div class="brand"><span class="brand-dot"></span>Velmont Recycling</div>
  <div class="follow">FOLLOW US <span class="soc"></span><span class="soc b"></span><span class="soc c"></span></div>
  <div class="callnow">
    <svg class="ph" viewBox="0 0 24 24"><path d="M6.6 10.8a15 15 0 006.6 6.6l2.2-2.2c.3-.3.7-.4 1-.2 1.1.4 2.3.6 3.6.6.6 0 1 .4 1 1V20c0 .6-.4 1-1 1A17 17 0 013 4c0-.6.4-1 1-1h3.5c.6 0 1 .4 1 1 0 1.3.2 2.5.6 3.6.1.3 0 .7-.2 1z" fill="#1f5fae"/></svg>
    <div><small>CALL US NOW</small><strong>(512) 555-0147</strong></div>
  </div>
  <nav class="nav"><a class="active" href="#">HOME</a><a href="#">ABOUT US</a><a href="#">SERVICES</a><a href="#">TESTIMONIALS</a><a href="#">CONTACT US</a></nav>
</header>

<section class="hero" role="img" aria-label="Close-up photograph of green and blue computer circuit boards">
  <h1 class="hero-title">COMPUTER<br>RECYCLING MADE EASY</h1>
  <a class="btn" href="#">READ MORE</a>
  <div class="dots"><i></i><i></i><i></i><i></i></div>
</section>

<div class="feature" style="top:740px"><span class="ic"><svg width="40" height="40" viewBox="0 0 40 40"><circle cx="20" cy="20" r="15" fill="none" stroke="#555" stroke-width="3"/><path d="M20 10v10l7 4" stroke="#555" stroke-width="3" fill="none"/></svg></span><span>Save time<br>and money</span></div>
<div class="feature-rule" style="top:855px"></div>
<div class="feature" style="top:890px"><span class="ic"><svg width="40" height="40" viewBox="0 0 40 40"><path d="M20 6l14 24H6z" fill="none" stroke="#555" stroke-width="3" stroke-linejoin="round"/></svg></span><span>Reduce Risk &amp;<br>achieve compliance</span></div>
<div class="feature-rule" style="top:1005px"></div>
<div class="feature" style="top:1040px"><span class="ic"><svg width="40" height="40" viewBox="0 0 40 40"><path d="M32 20a12 12 0 01-21 8M8 20a12 12 0 0121-8" fill="none" stroke="#555" stroke-width="3"/><path d="M29 6v7h-7M11 34v-7h7" fill="none" stroke="#555" stroke-width="3"/></svg></span><span>Maximize value<br>recovery</span></div>
<div class="vrule"></div>

<section class="welcome">
  <h3>WELCOME TO</h3>
  <h2>VELMONT RECYCLING</h2>
  <p>What most people do not realize is electronic waste represents 2% of America's trash in landfills, but it equals 70% of overall toxic waste. Used computer equipment is a rapidly growing source of waste across the country.</p>
  <p>Only 12.5% of electronic waste is currently recycled in the US. Computers contain valuable parts that we can recycle, and heavy metals that we should try to keep out of landfills. Despite this, Texas has historically had low computer recycling rates in the past.</p>
  <a class="btn" href="#">READ MORE</a>
</section>

<section class="services">
  <svg class="slant" width="1200" height="40"><polygon points="0,40 1200,0 1200,0 0,0" fill="#fff"/></svg>
  <h2 class="sec-title" style="top:96px">Our Services</h2>
  <div class="grid-v" style="left:450px;top:220px;height:500px"></div>
  <div class="grid-v" style="left:760px;top:220px;height:500px"></div>
  <div class="grid-h" style="left:150px;top:432px;width:900px"></div>

  <div class="svc" style="left:155px;top:210px">
    <svg width="64" height="48" viewBox="0 0 64 48"><rect x="16" y="8" width="30" height="24" fill="#1f5fae"/><path d="M46 16h9l7 9v7H46z" fill="#1f5fae"/><circle cx="24" cy="36" r="5" fill="#1f5fae"/><circle cx="52" cy="36" r="5" fill="#1f5fae"/><path d="M2 14h10M5 20h10M2 26h10" stroke="#1f5fae" stroke-width="2.5"/></svg>
    <h4>E-Waste Pickups,<br>Cleanouts &amp; Liquidations</h4>
    <p>Sed ut perspiciatis unde omnis iste natus error sit voluptatem accus antium doloremque laudantium, totam</p>
  </div>
  <div class="svc" style="left:450px;top:210px">
    <svg width="64" height="48" viewBox="0 0 64 48"><rect x="6" y="4" width="40" height="28" fill="none" stroke="#1f5fae" stroke-width="4"/><rect x="20" y="34" width="12" height="4" fill="#1f5fae"/><rect x="14" y="40" width="24" height="4" fill="#1f5fae"/><rect x="42" y="20" width="18" height="24" fill="#1f5fae"/></svg>
    <h4>Electronic Equipment<br>Recovery &amp; Refurbishment</h4>
    <p>Sed ut perspiciatis unde omnis iste natus error sit voluptatem accus antium doloremque laudantium, totam</p>
  </div>
  <div class="svc" style="left:758px;top:210px">
    <svg width="64" height="48" viewBox="0 0 64 48"><ellipse cx="32" cy="8" rx="16" ry="6" fill="#1f5fae"/><rect x="16" y="14" width="32" height="9" rx="4" fill="#1f5fae"/><rect x="16" y="25" width="32" height="9" rx="4" fill="#1f5fae"/><rect x="16" y="36" width="32" height="9" rx="4" fill="#1f5fae"/></svg>
    <h4>Certified<br>Data Destruction</h4>
    <p>Sed ut perspiciatis unde omnis iste natus error sit voluptatem accus antium doloremque laudantium, totam</p>
  </div>
  <div class="svc" style="left:155px;top:470px">
    <svg width="64" height="48" viewBox="0 0 64 48"><path d="M32 4a20 20 0 0118 12M50 32a20 20 0 01-18 12M14 32A20 20 0 0114 16" fill="none" stroke="#1f5fae" stroke-width="5"/></svg>
    <h4>Electronics &amp;<br>Metal Recycling</h4>
    <p>Sed ut perspiciatis unde omnis iste natus error sit voluptatem accus antium doloremque laudantium, totam</p>
  </div>
  <div class="svc" style="left:450px;top:470px">
    <svg width="64" height="48" viewBox="0 0 64 48"><path d="M8 24L32 4l24 20" fill="none" stroke="#1f5fae" stroke-width="5"/><rect x="16" y="24" width="32" height="20" fill="#1f5fae"/></svg>
    <h4>In-House Electronic<br>Waste Processing</h4>
    <p>Sed ut perspiciatis unde omnis iste natus error sit voluptatem accus antium doloremque laudantium, totam</p>
  </div>
  <div class="svc" style="left:758px;top:470px">
    <svg width="64" height="48" viewBox="0 0 64 48"><rect x="10" y="4" width="40" height="30" fill="none" stroke="#1f5fae" stroke-width="4"/><rect x="24" y="36" width="12" height="8" fill="#1f5fae"/><rect x="44" y="14" width="16" height="30" fill="#1f5fae"/></svg>
    <h4>CRT tvs &amp; Monitors<br>Recycling</h4>
    <p>Sed ut perspiciatis unde omnis iste natus error sit voluptatem accus antium doloremque laudantium, totam</p>
  </div>
</section>

<svg class="abs" style="left:0;top:1950px" width="1200" height="700" viewBox="0 0 1200 700">
  <path d="M430 205 C320 205 285 250 285 330 V380" fill="none" stroke="#f5b642" stroke-width="2"/>
  <path d="M770 205 C880 205 915 250 915 330 V380" fill="none" stroke="#f5b642" stroke-width="2"/>
  <path d="M477 380 V330 C477 300 500 290 520 290" fill="none" stroke="#f5b642" stroke-width="2"/>
  <path d="M655 380 V330 C655 300 680 290 700 290" fill="none" stroke="#f5b642" stroke-width="2"/>
  <circle cx="600" cy="205" r="165" fill="#fff"/>
  <circle cx="600" cy="205" r="150" fill="none" stroke="#f5900f" stroke-width="22" stroke-dasharray="236 707" transform="rotate(-180 600 205)"/>
  <circle cx="600" cy="205" r="150" fill="none" stroke="#1b8a9a" stroke-width="22" stroke-dasharray="0 236 236 707" transform="rotate(-180 600 205)"/>
  <circle cx="600" cy="205" r="150" fill="none" stroke="#0f3e5e" stroke-width="22" stroke-dasharray="0 472 236 707" transform="rotate(-180 600 205)"/>
  <circle cx="600" cy="205" r="150" fill="none" stroke="#e2332c" stroke-width="22" stroke-dasharray="0 708 236 707" transform="rotate(-180 600 205)"/>
  <circle cx="600" cy="205" r="128" fill="#fff"/>
  <path d="M600 110a30 30 0 0126 15M626 155a30 30 0 01-26 15M574 155a30 30 0 010-30" fill="none" stroke="#2ca24a" stroke-width="8"/>
  <text x="600" y="246" text-anchor="middle" font-family="Montserrat,sans-serif" font-weight="700" font-size="26" fill="#222">CAPABILITY</text>

  <line x1="196" y1="463" x2="935" y2="463" stroke="#ddd" stroke-width="2"/>
  <circle cx="196" cy="463" r="12" fill="#555"/>
  <circle cx="935" cy="463" r="12" fill="#555"/>

  <circle cx="292" cy="463" r="70" fill="#fff" stroke="#eee" stroke-width="3"/><circle cx="292" cy="463" r="62" fill="#f5900f"/>
  <rect x="268" y="448" width="32" height="24" fill="none" stroke="#fff" stroke-width="3"/><path d="M300 456h10l6 8v8h-16z" fill="none" stroke="#fff" stroke-width="3"/>
  <circle cx="477" cy="463" r="70" fill="#fff" stroke="#eee" stroke-width="3"/><circle cx="477" cy="463" r="62" fill="#1b8a9a"/>
  <path d="M477 440a22 22 0 0119 11M496 474a22 22 0 01-19 11M458 474a22 22 0 010-22" fill="none" stroke="#fff" stroke-width="5"/>
  <circle cx="655" cy="463" r="70" fill="#fff" stroke="#eee" stroke-width="3"/><circle cx="655" cy="463" r="62" fill="#0f3e5e"/>
  <rect x="638" y="440" width="34" height="42" fill="none" stroke="#fff" stroke-width="3"/><circle cx="655" cy="460" r="8" fill="none" stroke="#fff" stroke-width="3"/>
  <circle cx="840" cy="463" r="70" fill="#fff" stroke="#eee" stroke-width="3"/><circle cx="840" cy="463" r="62" fill="#e2332c"/>
  <path d="M860 470a22 22 0 11-6-22" fill="none" stroke="#fff" stroke-width="5"/><path d="M846 438l10 10-12 4z" fill="#fff"/>

  <g stroke-width="2" stroke-dasharray="3 5">
    <line x1="292" y1="540" x2="292" y2="650" stroke="#f5900f"/>
    <line x1="477" y1="540" x2="477" y2="650" stroke="#1b8a9a"/>
    <line x1="655" y1="540" x2="655" y2="650" stroke="#0f3e5e"/>
    <line x1="840" y1="540" x2="840" y2="650" stroke="#e2332c"/>
  </g>
  <circle cx="292" cy="560" r="8" fill="#f5900f"/><circle cx="477" cy="560" r="8" fill="#1b8a9a"/><circle cx="655" cy="560" r="8" fill="#0f3e5e"/><circle cx="840" cy="560" r="8" fill="#e2332c"/>
  <path d="M283 655h18l-9 12z" fill="#f5900f"/><path d="M468 655h18l-9 12z" fill="#1b8a9a"/><path d="M646 655h18l-9 12z" fill="#0f3e5e"/><path d="M831 655h18l-9 12z" fill="#e2332c"/>
</svg>

<div class="cap-list" style="left:224px;top:2650px"><h5>Logistics</h5>Global Logistics Support<br>Global Warehouse Capabilities<br>Global Audit Capabilities<br>Inventory Management<br>Asset Management<br>Bill of Lading<br>Proof of Delivery<br>Transfer of Ownership (TOO)</div>
<div class="cap-list" style="left:428px;top:2650px"><h5>Recycling</h5>Certified Global Recycling Capabilities<br>Sort by commodity<br>Certificate of Recycling<br>Data Destruction<br>Verifiable Certified Downstream Vendors</div>
<div class="cap-list" style="left:619px;top:2650px"><h5>Certificates</h5>R2:2013 Responsible Recycling Certified<br>ISO 14001:2015<br>OHSAS 18001:2007<br>State Environmental Quality Board (SEQB)<br>Regulated Entity # RN220480917<br>SOPR Compliant<br>HIPPA Compliant</div>
<div class="cap-list" style="left:813px;top:2650px"><h5>Return</h5>Market Value Pricing<br>Profit Sharing</div>

<h2 class="sec-title" style="top:2938px">Benefit</h2>
<section class="benefit-band">
  <div class="half2"></div>
  <svg class="abs" style="left:578px;top:0" width="44" height="22"><polygon points="0,0 44,0 22,22" fill="#fff"/></svg>
  <div class="benefit-col" style="left:170px">
    <div class="hd"><svg width="64" height="40" viewBox="0 0 64 40"><rect x="2" y="6" width="36" height="24" fill="#fff"/><path d="M38 12h12l10 10v8H38z" fill="#fff"/><circle cx="14" cy="34" r="5" fill="#fff"/><circle cx="50" cy="34" r="5" fill="#fff"/></svg><span>PICKUPS AND<br>CLEANOUTS!</span></div>
    <ul><li>Sed ut perspiciatis unde omnis</li><li>But I must explain to you how all this mistaken idea of denouncing pleasure and praisin.</li><li>At vero eos et accusamus et iusto odio dignissimos ducimus qui blanditiis praesentium</li></ul>
    <a class="btn-w" href="#">READ MORE</a>
  </div>
  <div class="benefit-col" style="left:668px">
    <div class="hd"><svg width="50" height="56" viewBox="0 0 50 56"><circle cx="25" cy="24" r="13" fill="#fff"/><rect x="19" y="38" width="12" height="10" fill="#fff"/><path d="M25 2v5M6 10l4 4M44 10l-4 4M1 24h5M44 24h5" stroke="#fff" stroke-width="3"/></svg><span>A RECYCLING<br>PLAN FOR YOU</span></div>
    <ul><li>Sed ut perspiciatis unde omnis</li><li>But I must explain to you how all this mistaken idea of denouncing pleasure and praisin.</li><li>At vero eos et accusamus et iusto odio dignissimos ducimus qui blanditiis praesentium</li></ul>
    <a class="btn-w" href="#">CONTACT US TODAY</a>
  </div>
</section>

<section class="help">
  <div class="q">NEED HELP? <span>CALL US:</span></div>
  <div class="num">(512) 555-0147</div>
  <div class="sep"></div>
  <div class="sub">SUBSCRIBE <span>NEWSLETTER</span></div>
  <form><input type="text" placeholder="E-mail id"><button type="button">➜</button></form>
</section>

<footer class="site-footer">
  <div class="brand"><span class="brand-dot"></span>Velmont Recycling</div>
  <div class="fcol" style="left:510px">
    <h6>CONTACT US</h6>
    <div class="row"><span>●</span><span>2150 Larkspur Row<br>Austin TX USA 78751</span></div>
    <div class="row"><span>●</span><span>(512) 555-0147</span></div>
    <div class="row"><span>✉</span><span>hello@velmontrecycling.com</span></div>
  </div>
  <div class="fcol" style="left:745px">
    <h6>MENU</h6>Home<br>About Us<br>Services<br>Testimonials<br>Contact Us
  </div>
  <div class="fcol" style="left:935px">
    <h6>CONNECT WITH US</h6>
    <div class="sr"><span class="soc"></span>Friendbook</div>
    <div class="sr"><span class="soc b"></span>Chirper</div>
    <div class="sr"><span class="soc c"></span>WorkNet</div>
  </div>
  <div class="copy-rule"></div>
  <div class="copy">Copyrights @ 2018 All Rights Reserved</div>
</footer>

</body>
</html>
```